Folder outside surface for Marlowe Eye Studios

Hello :
Attached, please see the images and logo that are meant for a 9x12 inch folder. I need a 300dpi file (png, jpeg, and vector) that fits the diagram from a printing company.

```html
<!DOCTYPE html>
<html lang="en">
<head>
<meta charset="utf-8">
<title>Marlowe Eye Studios – Folder Outside Surface</title>
<link rel="stylesheet" href="https://fonts.googleapis.com/css2?family=Poppins:wght@600;700&display=swap">
<style>
  :root{
    --stage:#a5a6aa;
    --paper:#ffffff;
    --navy:#153b73;
    --teal:#02b1c1;
    --orange:#e95504;
    --white:#ffffff;
  }
  *{margin:0;padding:0;box-sizing:border-box}
  html,body{width:1200px;height:808px;overflow:hidden;background:var(--stage)}
  body{position:relative;font-family:"Poppins",sans-serif}
  .folder-face{position:absolute;top:82px;width:476px;height:636px;background:var(--paper);overflow:hidden}
  .folder-front{left:83px}
  .folder-back{left:640px}
  .band-art{position:absolute;left:0;top:0;width:476px;height:636px;display:block}

  .brand-block{position:absolute;left:0;width:476px;top:128px;text-align:center;color:var(--navy);font-weight:700}
  .brand-dot{display:block;width:78px;height:78px;border-radius:50%;background:var(--orange);margin:0 auto 26px}
  .brand-name{display:block;font-size:40px;line-height:40px;letter-spacing:.5px}
  .brand-sub{display:block;font-size:24px;line-height:26px;margin-top:8px;letter-spacing:1px}

  .tagline{position:absolute;left:0;width:476px;text-align:center;color:var(--white);font-weight:600;white-space:nowrap}
  .folder-front .tagline{top:556px;font-size:18.5px}
  .folder-back .tagline{top:484px;font-size:21px}

  .mini-brand{position:absolute;left:310px;top:578px;display:flex;align-items:center;gap:7px;color:var(--white);font-weight:700}
  .mini-dot{width:26px;height:26px;border-radius:50%;background:var(--orange)}
  .mini-text{border-left:1px solid var(--white);padding-left:6px;line-height:1}
  .mini-text span{display:block}
  .mini-name{font-size:13px}
  .mini-sub{font-size:7.5px;margin-top:2px;letter-spacing:.3px}
</style>
</head>
<body>

<section class="folder-face folder-front">
  <svg class="band-art" viewBox="0 0 476 636" aria-hidden="true">
    <path fill="var(--orange)" d="M0 440 Q238 400 476 440 L476 454 Q238 414 0 454 Z"/>
    <path fill="var(--teal)" d="M0 462 Q238 422 476 462 L476 480 Q238 440 0 480 Z"/>
    <path fill="var(--navy)" d="M0 490 Q238 450 476 490 L476 636 L0 636 Z"/>
  </svg>
  <div class="brand-block">
    <span class="brand-dot"></span>
    <span class="brand-name">MARLOWE</span>
    <span class="brand-sub">EYE STUDIOS</span>
  </div>
  <p class="tagline">Clear Sight. Careful Hands.</p>
</section>

<section class="folder-face folder-back">
  <svg class="band-art" viewBox="0 0 476 636" aria-hidden="true">
    <rect x="0" y="420" width="476" height="6" fill="var(--orange)"/>
    <rect x="0" y="426" width="476" height="10" fill="var(--teal)"/>
    <rect x="0" y="436" width="476" height="200" fill="var(--navy)"/>
  </svg>
  <p class="tagline">Clear Sight. Careful Hands.</p>
  <div class="mini-brand">
    <span class="mini-dot"></span>
    <div class="mini-text">
      <span class="mini-name">MARLOWE</span>
      <span class="mini-sub">EYE STUDIOS</span>
    </div>
  </div>
</section>

</body>
</html>
```